Brevik Electric Business Card

An electrical contractor needs a business card design, that will stand out.
I would like designs that use the colors in the logo shown. The logo attached I am ok with but if you have a better idea I am open for suggestions. I like the color scheme.
Industry/Entity Type
Electrical
Contact Information for Business Card
Services, social media, QR code,

```html
<!DOCTYPE html>
<html lang="en">
<head>
<meta charset="utf-8">
<title>Brevik Electric Business Card</title>
<link rel="stylesheet" href="https://fonts.googleapis.com/css2?family=Montserrat:wght@400;500;700&display=swap">
<style>
  :root {
    --bg: #a9a9ab;
    --card: #231f21;
    --card-back: #201c1e;
    --gold: #f0b510;
    --orange: #f39a12;
    --white: #ffffff;
    --muted: #d9d6d7;
  }
  * { box-sizing: border-box; margin: 0; padding: 0; }
  html, body { width: 1200px; height: 800px; overflow: hidden; }
  body {
    background: var(--bg);
    font-family: "Montserrat", Arial, sans-serif;
    display: flex;
    align-items: center;
    justify-content: center;
    gap: 60px;
  }
  .card {
    position: relative;
    width: 520px;
    height: 297px;
    border-radius: 18px;
    overflow: hidden;
    box-shadow: 0 14px 30px rgba(0,0,0,0.35);
  }
  .card-front { background: var(--card); color: var(--white); }
  .brand {
    position: absolute;
    right: 34px;
    top: 46px;
    display: flex;
    align-items: center;
    gap: 12px;
  }
  .brand-square {
    width: 26px; height: 26px;
    border-radius: 5px;
    background: var(--gold);
  }
  .brand-name {
    font-weight: 700;
    font-size: 22px;
    letter-spacing: 0.5px;
    color: var(--white);
  }
  .divider {
    position: absolute;
    left: 40px; right: 34px; top: 150px;
    height: 1px;
    background: var(--gold);
  }
  .person {
    position: absolute;
    left: 40px;
    top: 104px;
  }
  .person-name {
    font-weight: 700;
    font-size: 20px;
    color: var(--gold);
    letter-spacing: 0.4px;
  }
  .person-title {
    font-size: 12px;
    font-weight: 500;
    color: var(--white);
    margin-top: 3px;
  }
  .contacts {
    position: absolute;
    left: 40px;
    top: 164px;
    list-style: none;
    font-size: 12px;
    line-height: 19px;
  }
  .contacts li { display: flex; align-items: center; gap: 9px; }
  .contacts svg { width: 11px; height: 11px; flex: none; }
  .address {
    position: absolute;
    right: 34px;
    top: 164px;
    text-align: right;
    font-size: 12px;
    line-height: 19px;
  }
  .address .web { color: var(--gold); }
  .edge-band {
    position: absolute;
    left: 0; right: 0; bottom: 0;
    height: 9px;
    display: flex;
  }
  .edge-band .gold { flex: 0 0 56%; background: var(--gold); }
  .edge-band .white { flex: 1; background: var(--white); }

  .card-back { background: var(--card-back); }
  .back-pattern {
    position: absolute;
    inset: 0;
    background: linear-gradient(200deg, #141213 0%, #2a2527 55%, #3a3336 100%);
  }
  .back-brand {
    position: absolute;
    right: 34px;
    bottom: 34px;
    display: flex;
    align-items: center;
    gap: 8px;
  }
  .back-brand .brand-square { width: 16px; height: 16px; border-radius: 3px; background: var(--orange); }
  .back-brand .brand-name { font-size: 13px; }
</style>
</head>
<body>
  <section class="card card-front" aria-label="Business card front">
    <div class="brand">
      <span class="brand-square"></span>
      <span class="brand-name">BREVIK ELECTRIC</span>
    </div>

    <div class="person">
      <p class="person-name">DANIEL HARPER</p>
      <p class="person-title">President</p>
    </div>

    <div class="divider"></div>

    <ul class="contacts">
      <li>
        <svg viewBox="0 0 12 12" aria-hidden="true"><path d="M2.5 1h2l1 3-1.3 1a6 6 0 0 0 2.8 2.8l1-1.3 3 1v2a1 1 0 0 1-1 1A9.5 9.5 0 0 1 1.5 2a1 1 0 0 1 1-1z" fill="var(--gold)"/></svg>
        555-214-0187
      </li>
      <li>
        <svg viewBox="0 0 12 12" aria-hidden="true"><rect x="1.5" y="1.5" width="9" height="9" fill="none" stroke="var(--gold)" stroke-width="1.5"/></svg>
        555-512-7730
      </li>
      <li>
        <svg viewBox="0 0 12 12" aria-hidden="true"><rect x="3" y="0.5" width="6" height="11" rx="1" fill="var(--gold)"/><rect x="4" y="2" width="4" height="6.5" fill="var(--card)"/></svg>
        555-325-4419
      </li>
      <li>
        <svg viewBox="0 0 12 12" aria-hidden="true"><rect x="0.5" y="2" width="11" height="8" fill="var(--gold)"/><path d="M0.8 2.4 6 6.6l5.2-4.2" fill="none" stroke="var(--card)" stroke-width="1"/></svg>
        info@brevikelectric.com
      </li>
    </ul>

    <div class="address">
      <p>Brevik Electric Group</p>
      <p>4120 Alder Creek Road</p>
      <p>Juneau, Alaska 99801</p>
      <p class="web">www.brevikelectric.com</p>
    </div>

    <div class="edge-band"><span class="gold"></span><span class="white"></span></div>
  </section>

  <section class="card card-back" aria-label="Business card back">
    <div class="back-pattern" role="img" aria-label="Repeating tonal pattern of brand marks across the card back"></div>
    <div class="back-brand">
      <span class="brand-square"></span>
      <span class="brand-name">BREVIK ELECTRIC</span>
    </div>
  </section>
</body>
</html>
```